Modern and Improved business card design for Family Dental Practice

We have 2 sets of logo we have designed and now just need a business card layout and design for the office. Colors are on the logo. We can choose which logo we want to go with . The font can be changed to whatever seems modern and relevant. We are family dental office that has been open for over 15 years in South Austin Texas.

Target Market(s)

Handout Business cards to referrals and specialists

Industry/Entity Type

Dental

Contact Information for Business Card

We need address, phone, website and email address. 4830 North Maple Loop Suite 208 , Austin,Texas 78392....phone: 512-847-3195.....email- info@bluepinedental.example....website - BluePineDental.example

Font styles to use
Serif
Decorative

Requirements
Must have
• my logo. We have 2 logos, but we can use just one or if we can incorporate one on one side and the other on the other side.
Nice to have
• Really just need a modern look and clean that incorporates the logo and colors .

```html
<!DOCTYPE html>
<html lang="en">
<head>
<meta charset="utf-8">
<title>Blue Pine Family Dentistry – Business Card</title>
<link href="https://fonts.googleapis.com/css2?family=Arimo:wght@400;700&display=swap" rel="stylesheet">
<style>
  :root {
    --backdrop: #b9b8b3;
    --card: #ffffff;
    --brand-green: #2e8b3e;
    --leaf-green: #7aa33a;
    --ink: #3a3a3a;
    --rule: #8a8a8a;
    --edge: #237a35;
  }
  * { box-sizing: border-box; margin: 0; padding: 0; }
  html, body { width: 1200px; height: 857px; overflow: hidden; }
  body {
    background: var(--backdrop);
    font-family: "Arimo", Arial, sans-serif;
    position: relative;
  }
  .card {
    position: absolute;
    width: 520px;
    height: 297px;
    background: var(--card);
    border-bottom: 3px solid var(--edge);
    box-shadow: 0 10px 24px rgba(0,0,0,.22);
  }
  .card--front { left: 60px; top: 150px; display: flex; align-items: center; }
  .card--back { left: 620px; top: 410px; display: flex; align-items: center; justify-content: center; }

  .brand { width: 250px; display: flex; align-items: center; justify-content: center; gap: 14px; }
  .brand__dot { width: 34px; height: 34px; border-radius: 50%; background: var(--brand-green); flex: none; }
  .brand__name {
    font-size: 22px; line-height: 1.1; font-weight: 400; color: var(--ink);
    text-transform: uppercase; letter-spacing: .5px;
  }

  .divider { width: 1px; height: 130px; background: var(--rule); }

  .contact { padding-left: 24px; color: var(--ink); font-size: 12.5px; line-height: 1.4; }
  .contact__name { color: var(--brand-green); font-size: 16px; font-weight: 700; letter-spacing: .5px; }
  .contact__role { margin-bottom: 8px; }
  .contact__address { margin-bottom: 8px; }
  .contact__line { display: flex; align-items: center; gap: 8px; }
  .contact__line svg { width: 11px; height: 11px; flex: none; fill: var(--leaf-green); }

  .back-brand { display: flex; align-items: center; gap: 16px; }
  .back-brand__square { width: 40px; height: 40px; background: var(--leaf-green); }
  .back-brand__name { font-size: 26px; color: var(--ink); letter-spacing: 1px; }
</style>
</head>
<body>
  <section class="card card--front">
    <div class="brand">
      <span class="brand__dot"></span>
      <span class="brand__name">Blue Pine<br>Family Dentistry</span>
    </div>
    <div class="divider"></div>
    <div class="contact">
      <p class="contact__name">DANIEL REYES</p>
      <p class="contact__role">Operational Manager</p>
      <p class="contact__address">4830 North Maple Loop, Suite 208<br>Austin, Texas 78392</p>
      <p class="contact__line">
        <svg viewBox="0 0 24 24"><path d="M6.6 10.8a15 15 0 0 0 6.6 6.6l2.2-2.2c.3-.3.7-.4 1-.2 1.1.4 2.3.6 3.6.6.6 0 1 .4 1 1V20c0 .6-.4 1-1 1A17 17 0 0 1 3 4c0-.6.4-1 1-1h3.5c.6 0 1 .4 1 1 0 1.3.2 2.5.6 3.6.1.3 0 .7-.2 1z"/></svg>
        512-847-3195
      </p>
      <p class="contact__line">
        <svg viewBox="0 0 24 24"><path d="M2 5h20v14H2z M2 5l10 8 10-8" /></svg>
        info@bluepinedental.example
      </p>
      <p class="contact__line">
        <svg viewBox="0 0 24 24"><circle cx="12" cy="12" r="10"/></svg>
        BluePineDental.example
      </p>
    </div>
  </section>

  <section class="card card--back">
    <div class="back-brand">
      <span class="back-brand__square"></span>
      <span class="back-brand__name">Blue Pine Family Dentistry</span>
    </div>
  </section>
</body>
</html>
```